Window and door installer van signage

We're a new window and door installation company based in Edinburgh Scotland. We are looking for a design to go on our van to promote our our services. The name of the company is Brambleford Joinery. services it must include are
1. U-PVC windows
2. U-PVC Doors
3. Composite Doors
4. Timber windows
5. Timber Doors
6. New sash and case
7. Misted unit replacement
8. French and Patio Doors
We already have a logo but I don't mind slight changes to it. I've included a photo of it as well as the van.

```html
<!DOCTYPE html>
<html lang="en">
<head>
<meta charset="utf-8">
<title>Brambleford Joinery – Van Signage</title>
<link rel="stylesheet" href="https://fonts.googleapis.com/css2?family=Poppins:wght@300;400;500;600&display=swap">
<style>
  :root {
    --page: #e6e6e6;
    --panel-blue: #37698c;
    --panel-dark: #333845;
    --white: #ffffff;
    --navy: #1f2a7a;
    --gold: #c9a15a;
    --dot-red: #c8102e;
    --dot-lime: #c6d12a;
    --dot-blue: #1a3fd6;
    --dot-magenta: #c72bd1;
    --photo-light: #cfc3b0;
    --photo-dark: #6e6456;
  }
  * { box-sizing: border-box; margin: 0; padding: 0; }
  html, body { width: 799px; height: 1200px; overflow: hidden; }
  body {
    background: var(--page);
    font-family: "Poppins", sans-serif;
    color: var(--white);
    position: relative;
  }
  .signage {
    position: absolute;
    left: 20px;
    width: 760px;
    overflow: hidden;
  }
  .signage--blue { top: 297px; height: 267px; background: var(--panel-blue); }
  .signage--dark { top: 594px; height: 308px; background: var(--panel-dark); }

  .signage > * { position: absolute; }
  .photo-frame { left: 0; top: 0; width: 760px; height: 100%; }

  .logo-box {
    background: var(--white);
    color: var(--navy);
    display: flex; flex-direction: column; align-items: center; justify-content: flex-end;
    text-align: center; font-weight: 400; line-height: 1.15;
    padding-bottom: 7px;
  }
  .logo-box .mark { width: 18px; height: 18px; border-radius: 50%; background: var(--navy); margin-bottom: 6px; }

  .website { font-size: 5.5px; letter-spacing: 0.08em; display: flex; align-items: center; gap: 3px; transform: translateY(-50%); white-space: nowrap; }
  .globe { width: 7px; height: 7px; flex: none; }
  .social { display: flex; gap: 3px; transform: translateY(-50%); }
  .social span { width: 7px; height: 7px; background: var(--white); border-radius: 1px; }

  .rule { height: 1px; background: rgba(255,255,255,0.75); }
  .rule--dot::after {
    content: ""; position: absolute; left: 60%; top: -1px; width: 3px; height: 3px; background: var(--white);
  }

  .headline { line-height: 1.2; letter-spacing: 0.04em; }
  .headline .light { display: block; font-weight: 300; }
  .headline .bold { display: block; font-weight: 600; }

  .service { display: flex; align-items: center; font-weight: 500; letter-spacing: 0.05em; white-space: nowrap; transform: translateY(-50%); }
  .service .ring { border: 1.4px solid var(--white); border-radius: 50%; flex: none; }
  .service .ring--red { border-color: var(--dot-red); }
  .service .ring--lime { border-color: var(--dot-lime); }
  .service .ring--blue { border-color: var(--dot-blue); }
  .service .ring--magenta { border-color: var(--dot-magenta); }

  .badge {
    border-radius: 50%; background: var(--white); color: #222;
    display: flex; flex-direction: column; align-items: center; justify-content: center;
    font-weight: 600; line-height: 1; transform: rotate(-12deg);
  }
  .badge small { font-size: 3.2px; letter-spacing: 0.05em; margin-top: 1px; }

  .price-tag {
    border: 1px solid var(--gold); color: var(--gold);
    display: flex; align-items: center; justify-content: center; font-size: 7.5px;
  }
  .price-tag::after {
    content: ""; position: absolute; right: 7px; bottom: -2px; width: 4px; height: 4px; background: var(--gold);
  }

  .contact-label { font-size: 8.5px; font-weight: 400; letter-spacing: 0.04em; transform: translateY(-50%); text-align: right; }
  .contact-phone { font-size: 11px; font-weight: 500; letter-spacing: 0.04em; transform: translateY(-50%); text-align: right; }

  /* blue panel positions */
  .signage--blue .logo-box { left: 440px; top: 0; width: 55px; height: 70px; font-size: 7.5px; }
  .signage--blue .website { right: 68px; top: 14px; }
  .signage--blue .social { right: 13px; top: 14px; }
  .signage--blue .rule--a { left: 392px; top: 83px; width: 62px; }
  .signage--blue .rule--b { left: 477px; top: 83px; width: 62px; }
  .signage--blue .rule--c { left: 392px; top: 140px; width: 62px; }
  .signage--blue .rule--d { left: 477px; top: 140px; width: 62px; }
  .signage--blue .headline { left: 392px; top: 98px; font-size: 12.5px; }
  .signage--blue .service { font-size: 9.5px; }
  .signage--blue .service .ring { width: 10px; height: 10px; margin-right: 4px; }
  .signage--blue .col-1 { left: 388px; }
  .signage--blue .col-2 { left: 518px; }
  .signage--blue .row-1 { top: 182px; } .signage--blue .row-2 { top: 197px; }
  .signage--blue .row-3 { top: 212px; } .signage--blue .row-4 { top: 227px; }
  .signage--blue .badge { left: 115px; top: 85px; width: 32px; height: 32px; font-size: 8px; }
  .signage--blue .price-tag { left: 121px; top: 232px; width: 56px; height: 20px; }
  .signage--blue .contact-label { right: 415px; top: 241px; }
  .signage--blue .contact-phone { right: 415px; top: 256px; }

  /* dark panel positions */
  .signage--dark .logo-box { left: 460px; top: 0; width: 50px; height: 63px; font-size: 7px; }
  .signage--dark .website { right: 115px; top: 11px; }
  .signage--dark .social { right: 65px; top: 11px; }
  .signage--dark .rule--a { left: 414px; top: 77px; width: 58px; }
  .signage--dark .rule--b { left: 494px; top: 77px; width: 58px; }
  .signage--dark .rule--c { left: 414px; top: 131px; width: 58px; }
  .signage--dark .rule--d { left: 494px; top: 131px; width: 58px; }
  .signage--dark .headline { left: 414px; top: 91px; font-size: 11.2px; }
  .signage--dark .service { font-size: 9px; }
  .signage--dark .service .ring { width: 9.5px; height: 9.5px; margin-right: 4px; }
  .signage--dark .col-1 { left: 411px; }
  .signage--dark .col-2 { left: 534px; }
  .signage--dark .row-1 { top: 170px; } .signage--dark .row-2 { top: 184px; }
  .signage--dark .row-3 { top: 198px; } .signage--dark .row-4 { top: 213px; }
  .signage--dark .badge { left: 192px; top: 120px; width: 30px; height: 30px; font-size: 7.5px; }
  .signage--dark .price-tag { left: 195px; top: 258px; width: 52px; height: 20px; }
  .signage--dark .contact-label { right: 392px; top: 267px; }
  .signage--dark .contact-phone { right: 392px; top: 280px; }
</style>
</head>
<body>

<section class="signage signage--blue">
  <svg class="photo-frame" viewBox="0 0 760 267" role="img" aria-label="Photo of a man hanging framed pictures on a wall beside a window, cropped into a slanted frame">
    <defs>
      <linearGradient id="photoToneBlue" x1="0" y1="0" x2="1" y2="1">
        <stop offset="0" stop-color="var(--photo-light)"/>
        <stop offset="1" stop-color="var(--photo-dark)"/>
      </linearGradient>
    </defs>
    <polygon points="87,112 296,52 296,176 87,248" fill="url(#photoToneBlue)"/>
    <line x1="87" y1="155" x2="296" y2="97" stroke="var(--panel-blue)" stroke-width="3"/>
    <line x1="87" y1="205" x2="296" y2="145" stroke="var(--panel-blue)" stroke-width="3"/>
    <line x1="150" y1="94" x2="150" y2="230" stroke="var(--panel-blue)" stroke-width="2"/>
    <line x1="215" y1="75" x2="215" y2="210" stroke="var(--panel-blue)" stroke-width="2"/>
  </svg>
  <div class="badge">100%<small>GUARANTEE</small></div>
  <div class="price-tag">Best Prices</div>
  <p class="contact-label">CONTACT US</p>
  <p class="contact-phone">0131 496 0721</p>

  <div class="logo-box"><span class="mark"></span>Brambleford<br>Joinery</div>
  <p class="website">
    <svg class="globe" viewBox="0 0 10 10"><circle cx="5" cy="5" r="4.3" fill="none" stroke="#fff"/><ellipse cx="5" cy="5" rx="1.8" ry="4.3" fill="none" stroke="#fff" stroke-width="0.8"/><line x1="0.7" y1="5" x2="9.3" y2="5" stroke="#fff" stroke-width="0.8"/></svg>
    WWW.BRAMBLEFORD.CO.UK
  </p>
  <div class="social"><span></span><span></span><span></span></div>

  <div class="rule rule--a"></div><div class="rule rule--b rule--dot"></div>
  <h1 class="headline"><span class="light">UNLOCKING ELEGANCE</span><span class="bold">ONE WINDOW AT A TIME</span></h1>
  <div class="rule rule--c"></div><div class="rule rule--d rule--dot"></div>

  <p class="service col-1 row-1"><span class="ring ring--red"></span>U-PVC WINDOWS</p>
  <p class="service col-1 row-2"><span class="ring ring--lime"></span>U-PVC DOORS</p>
  <p class="service col-1 row-3"><span class="ring ring--blue"></span>COMPOSITE DOORS</p>
  <p class="service col-1 row-4"><span class="ring ring--magenta"></span>TIMBER WINDOWS</p>
  <p class="service col-2 row-1"><span class="ring ring--red"></span>TIMBER DOORS</p>
  <p class="service col-2 row-2"><span class="ring ring--lime"></span>NEW SASH AND CASE</p>
  <p class="service col-2 row-3"><span class="ring ring--blue"></span>MISTED UNIT REPLACEMENT</p>
  <p class="service col-2 row-4"><span class="ring ring--magenta"></span>FRENCH AND PATIO DOORS</p>
</section>

<section class="signage signage--dark">
  <svg class="photo-frame" viewBox="0 0 760 308" role="img" aria-label="Photo of a man hanging framed pictures on a wall beside a window, cropped into a slanted frame">
    <defs>
      <linearGradient id="photoToneDark" x1="0" y1="0" x2="1" y2="1">
        <stop offset="0" stop-color="var(--photo-light)"/>
        <stop offset="1" stop-color="var(--photo-dark)"/>
      </linearGradient>
    </defs>
    <polygon points="166,153 363,88 363,207 166,274" fill="url(#photoToneDark)"/>
    <line x1="166" y1="195" x2="363" y2="130" stroke="var(--panel-dark)" stroke-width="3"/>
    <line x1="166" y1="240" x2="363" y2="175" stroke="var(--panel-dark)" stroke-width="3"/>
    <line x1="228" y1="133" x2="228" y2="255" stroke="var(--panel-dark)" stroke-width="2"/>
    <line x1="290" y1="112" x2="290" y2="235" stroke="var(--panel-dark)" stroke-width="2"/>
  </svg>
  <div class="badge">100%<small>GUARANTEE</small></div>
  <div class="price-tag">Best Prices</div>
  <p class="contact-label">CONTACT US</p>
  <p class="contact-phone">0131 496 0721</p>

  <div class="logo-box"><span class="mark"></span>Brambleford<br>Joinery</div>
  <p class="website">
    <svg class="globe" viewBox="0 0 10 10"><circle cx="5" cy="5" r="4.3" fill="none" stroke="#fff"/><ellipse cx="5" cy="5" rx="1.8" ry="4.3" fill="none" stroke="#fff" stroke-width="0.8"/><line x1="0.7" y1="5" x2="9.3" y2="5" stroke="#fff" stroke-width="0.8"/></svg>
    WWW.BRAMBLEFORD.CO.UK
  </p>
  <div class="social"><span></span><span></span><span></span></div>

  <div class="rule rule--a"></div><div class="rule rule--b rule--dot"></div>
  <h2 class="headline"><span class="light">UNLOCKING ELEGANCE</span><span class="bold">ONE WINDOW AT A TIME</span></h2>
  <div class="rule rule--c"></div><div class="rule rule--d rule--dot"></div>

  <p class="service col-1 row-1"><span class="ring ring--red"></span>U-PVC WINDOWS</p>
  <p class="service col-1 row-2"><span class="ring ring--lime"></span>U-PVC DOORS</p>
  <p class="service col-1 row-3"><span class="ring ring--blue"></span>COMPOSITE DOORS</p>
  <p class="service col-1 row-4"><span class="ring ring--magenta"></span>TIMBER WINDOWS</p>
  <p class="service col-2 row-1"><span class="ring ring--red"></span>TIMBER DOORS</p>
  <p class="service col-2 row-2"><span class="ring ring--lime"></span>NEW SASH AND CASE</p>
  <p class="service col-2 row-3"><span class="ring ring--blue"></span>MISTED UNIT REPLACEMENT</p>
  <p class="service col-2 row-4"><span class="ring ring--magenta"></span>FRENCH AND PATIO DOORS</p>
</section>

</body>
</html>
```